Whitcombe Framing Works - Card Design

I am looking to use the logo designs that you already did for me to develop a business card. I would like the card to have a black background and be double sided. I want white and green logo and text. I have attached an inspiration photo of a look that I like. I would like to use the Vertical Logo attached to take up the full front side of the card. On the back where I have my name and information, I would like to have the horizontal logo or maybe even just the image of the 'A' and trees without the text. I am open, but I am looking for something clean and simple and I want the green to really pop! Additional files can be found under Design #: 40593216

Target Market(s)

Homeowners

Industry/Entity Type

Construction

Contact Information for Business Card

Name: Marcus Pellow, Title: Project Manager, Phone: 831.555.0147, Email: whitcombeframingworks@mailbarn.net, address: 418 Juniper Ln, Felton, CA 95092, Lic# 2046318

Colors
00AB8E
00BBA5
67D7C9
C6EFE9
E9F9F6

Requirements
Nice to have
• I would like to see the logos that I have already got from SketchHarbor, though I am open to new ones

```html
<!DOCTYPE html>
<html lang="en">
<head>
<meta charset="utf-8">
<title>Whitcombe Framing Works – Business Card</title>
<link href="https://fonts.googleapis.com/css2?family=Nunito+Sans:wght@400;600;700;800&display=swap" rel="stylesheet">
<style>
  :root {
    --page: #e9e6e1;
    --card: #121212;
    --green: #6abf4b;
    --forest: #223d1e;
    --white: #ffffff;
    --font: "Nunito Sans", Arial, sans-serif;
  }
  * { box-sizing: border-box; margin: 0; padding: 0; }
  html, body { width: 1200px; height: 1200px; overflow: hidden; }
  body {
    background: var(--page);
    font-family: var(--font);
    position: relative;
  }
  .card {
    position: absolute;
    left: 200px;
    width: 800px;
    height: 457px;
    background: var(--card);
    border-radius: 28px;
    overflow: hidden;
  }
  .card--front { top: 90px; }
  .card--back { top: 653px; }

  /* Front */
  .lockup {
    position: absolute;
    left: 0; right: 0; top: 120px;
    text-align: center;
    color: var(--white);
  }
  .lockup__years {
    display: flex;
    justify-content: space-between;
    width: 430px;
    margin: 0 auto 18px;
  }
  .lockup__year {
    font-size: 13px;
    letter-spacing: 5px;
    color: var(--white);
    padding: 4px 6px;
    border-top: 1px solid var(--green);
    border-bottom: 1px solid var(--green);
  }
  .lockup__mark {
    display: inline-flex;
    align-items: center;
    gap: 18px;
  }
  .lockup__square {
    width: 46px; height: 46px;
    background: var(--green);
  }
  .lockup__name {
    font-size: 44px;
    font-weight: 800;
    color: var(--white);
    letter-spacing: 1px;
    line-height: 1.1;
  }
  .socials {
    position: absolute;
    left: 0; right: 0; top: 330px;
    display: flex;
    justify-content: center;
    align-items: center;
    gap: 20px;
    color: var(--green);
    font-weight: 800;
    font-size: 17px;
  }
  .socials__item { display: flex; align-items: center; gap: 7px; }
  .socials__dot {
    width: 22px; height: 22px; border-radius: 50%;
    background: var(--green);
  }

  /* Back */
  .contact {
    position: absolute;
    left: 56px; top: 52px;
    z-index: 2;
  }
  .contact__name {
    color: var(--green);
    font-size: 50px;
    font-weight: 700;
    line-height: 1;
  }
  .contact__title {
    color: var(--white);
    font-size: 17px;
    font-weight: 700;
    letter-spacing: 5px;
    margin-top: 10px;
  }
  .contact__phone {
    color: var(--white);
    font-size: 58px;
    font-weight: 700;
    line-height: 1;
    margin-top: 70px;
  }
  .contact__details {
    color: var(--green);
    font-size: 19px;
    font-weight: 800;
    line-height: 1.2;
    margin-top: 8px;
  }
  .brand-panel {
    position: absolute;
    right: 0; bottom: 0;
    width: 340px; height: 300px;
    background: var(--forest);
    border-top-left-radius: 6px;
  }
  .brand-panel__square {
    position: absolute;
    right: 40px; top: 40px;
    width: 110px; height: 110px;
    background: var(--white);
  }
  .brand-panel__name {
    position: absolute;
    left: 36px; right: 36px; bottom: 36px;
    color: var(--white);
    font-size: 30px;
    font-weight: 800;
    line-height: 1.1;
  }
</style>
</head>
<body>
  <section class="card card--front" aria-label="Card front">
    <div class="lockup">
      <div class="lockup__years">
        <span class="lockup__year">ESTD</span>
        <span class="lockup__year">2020</span>
      </div>
      <div class="lockup__mark">
        <span class="lockup__square" aria-hidden="true"></span>
        <span class="lockup__name">Whitcombe Framing Works</span>
      </div>
    </div>
    <div class="socials">
      <span>FIND US ON:</span>
      <span class="socials__item"><span class="socials__dot"></span>Folkfeed</span>
      <span class="socials__item"><span class="socials__dot"></span>Snapwell</span>
      <span class="socials__item"><span class="socials__dot"></span>Chirpline</span>
    </div>
  </section>

  <section class="card card--back" aria-label="Card back">
    <div class="brand-panel">
      <span class="brand-panel__square" aria-hidden="true"></span>
      <span class="brand-panel__name">Whitcombe Framing Works</span>
    </div>
    <div class="contact">
      <h1 class="contact__name">Marcus Pellow</h1>
      <p class="contact__title">PROJECT MANAGER</p>
      <p class="contact__phone">831.555.0147</p>
      <p class="contact__details">
        whitcombeframingworks@mailbarn.net<br>
        418 Juniper Ln, Felton, CA 95092,<br>
        Lic# 2046318
      </p>
    </div>
  </section>
</body>
</html>
```